ReDesign of Velmarix.example and Velmarix app

Velmarix:

Velmarix aims to be your own personal cloud of profile information with ability to share a part of it with others based on the consumer.

As we visit different sites and buy different products, apply for new jobs, on-board in a company or fill out a basic form at a doctors office, we end up entering the same information again and again albeit with some sections different based on where you are. For example, we enter some basic informaiton “AND” billing address on brindle, vs you enter some basic information “AND” work history on a job site.

What if you created a profile one time and then create justed avatars or keys to a combination of information and at different places use different keys to unlock that specific piece of information.

Use Case 1: Peter Hale applying for a job
Peter goes to task harbor, creates new login, enters where he lives, email, phone, then goes into the most tedious phase of entering work history. He realizes, he also needs to go to Quillrun.example and do the exact same thing and so on on any job site he visits in future.

With Velmarix
Peter goes to Velmarix, updates all his work history, personal information (No SSN or credit card). Now he creates a new “key” called “petersworkrequest” with a cryptic “keycode” and chooses to share personal information + work history for this key. He now goes to any job site to see a “VX” icon. He clicks on that, a pop-up box with key and keycode appears. He ONLY enters petersworkrequset and the keycode he had set, boom, all his work informaiton is auto-populated in task harbor. Immense savings in time for Peter.

Use Case 2: Sharing contact information
Peter meets a beautiful at a bar and thinks he needs to share his personal information but only has a 5 mintue window. He realizes, he has created a key named “Peter42” and has chosen to share his personal information only (no work information). She asks for contact number, he gives her is VX key. She pulls up VX app instead of contact list to add contact, plugs in Peter42 (and a key if peter decides to protect this key with a code) and boom, she has peters phone/email/picture (yes picture), chatterly blog and a contact is automatically created!!!!! She now can really associate this Peter from 8 other Peter’s in the bar!!

Use Case 3: Always stay connected
Peter is bored of Houston and decides to move to LA.He wants a local phone number for people to get in touch with them easily. But now he has to do the painful job of sending all his friends his updated number/contact address. If he had exchanged information with Velmarix key with his friends, his contact information with them is always in sync. TThe Velmarix app is intelligent to know that new information is available for the same profile key. As long as the passcode is the same, that information is automatically updated in the consumers contact list. Next time Peter’s friend picks up the phone, he just need so hit “DIAL”. The correct number is dialed. Along with that, his friends now also have his updated address information which he had shared with the key.

SECURITY
Anytime anyone views your profile using your profile key, you automatically get notified to your registered email address of someone pulling up your profile. If you think it’s suspicious, you can change the access code or set an access code to that public key.

where to go:
Go to http://velmarix.example
Register and play around with different views you can create for your profile with different access codes

Download
Velmarix app from pomelo appshelf or Vantor playshelf. We need a nice look and feel for the app as well.

Target Market(s)

students, careers, hiring companies, anyone starting online presence

Industry/Entity Type

Credit Card

Requirements
Must have

• convey message, simplistic, an app to consume data, always stay updated with friends emails etc
Nice to have
• logo should show a user and multiple facets of user for multiple consumers

```html
<!DOCTYPE html>
<html lang="en">
<head>
<meta charset="utf-8">
<title>Velmarix</title>
<link rel="stylesheet" href="https://fonts.googleapis.com/css2?family=Arvo:wght@400;700&family=PT+Serif&family=Roboto:wght@100;300;400&family=Source+Sans+3:wght@700&display=swap">
<style>
:root{
  --bg-deep:#141517;
  --yellow:#f6f23a;
  --white:#ffffff;
  --grey:#7b7c7e;
  --grey-light:#a9aaac;
  --band:#2b2d30;
  --field-line:#6a6b6d;
  --ink:#111214;
}
*{box-sizing:border-box;margin:0;padding:0}
html,body{width:1200px;height:1026px;overflow:hidden;background:var(--bg-deep)}
.page{position:relative;width:1200px;height:1026px;overflow:hidden;font-family:"Roboto",Arial,sans-serif;color:var(--grey-light)}
.backdrop{position:absolute;inset:0;background:radial-gradient(ellipse at 35% 40%,#2c2e31 0%,#1c1d20 45%,#121315 100%)}
.abs{position:absolute}

.brand{left:172px;top:22px;font-family:"Arvo",serif;font-size:44px;letter-spacing:-1px;color:var(--yellow);line-height:1}
.find{left:647px;top:37px;font-family:"Source Sans 3",sans-serif;font-weight:700;font-size:18px;color:var(--white)}
.find-field{left:757px;top:30px;width:271px;height:34px;border:1px solid var(--field-line);border-radius:4px;background:rgba(0,0,0,.35)}
.find-field svg{position:absolute;left:8px;top:6px}
.find-field .sep{position:absolute;left:37px;top:6px;height:20px;border-left:1px dotted var(--field-line)}

.nav{left:171px;top:166px;list-style:none;font-family:"PT Serif",serif;font-size:24px;line-height:1}
.nav li{display:block;margin-bottom:2px}
.nav a{display:inline-block;background:var(--white);color:#222;padding:5px 8px 4px;text-decoration:none;letter-spacing:.3px}
.nav .accent a{background:var(--yellow)}

.numeral text{font-family:"Roboto",sans-serif;font-weight:100;fill:var(--grey)}
.num-dot{width:8px;height:8px;background:var(--grey)}

.login-band{left:638px;top:114px;width:562px;height:55px;background:var(--band)}
.login-title{left:660px;top:116px;font-family:"Arvo",serif;font-size:40px;letter-spacing:-1.5px;color:var(--yellow);line-height:1.25}
.login-intro{left:660px;top:174px;width:370px;font-weight:300;font-size:18px;line-height:23px;color:var(--grey)}
.rule{left:660px;top:255px;width:362px;border-top:1px dotted #4a4b4d}
.field{left:660px;width:362px;height:41px;border:1px solid var(--field-line);border-radius:3px;background:rgba(0,0,0,.25);color:var(--white);font-weight:300;font-size:17px}
.field span{position:absolute;left:58px;top:10px}
.field .sep{position:absolute;left:47px;top:9px;height:22px;border-left:1px dotted var(--field-line)}
.field svg{position:absolute;left:13px;top:8px}
.options{left:661px;top:383px;font-weight:300;font-size:15px;color:var(--grey)}
.checkbox{display:inline-block;width:11px;height:11px;background:var(--grey);margin-right:9px;vertical-align:-1px}
.forgot{left:820px;top:383px;font-weight:300;font-size:15.5px;color:var(--grey)}
.forgot a{color:var(--yellow);text-decoration:underline}
.login-btn{left:661px;top:421px;width:145px;height:37px;background:var(--yellow);color:var(--ink);font-family:"Arvo",serif;font-weight:700;font-size:23px;text-align:center;line-height:38px;border-radius:2px}

.your{left:349px;top:515px;font-family:"Arvo",serif;font-weight:700;font-size:38px;color:var(--yellow);letter-spacing:-1px}
.job-tag{left:172px;top:563px;height:45px;width:228px;background:#32353a;color:var(--white);font-family:"Arvo",serif;font-weight:700;font-size:33px;line-height:46px;padding-left:11px;letter-spacing:-.5px}
.starts{left:405px;top:575px;font-family:"Arvo",serif;font-weight:700;font-size:24px;color:var(--white)}
.cta{left:614px;top:563px;width:349px;height:45px;background:#070708;color:var(--yellow);font-family:"Arvo",serif;font-weight:700;font-size:24px;line-height:46px;text-align:center;letter-spacing:.5px}
.cta-arrow{left:970px;top:567px}

.perk{top:740px;font-family:"Arvo",serif;font-weight:700;line-height:1}
.perk-lead{left:174px;font-size:43px;letter-spacing:-.5px;color:var(--grey)}
.perk-partner{left:452px;top:742px;font-size:40px;letter-spacing:-1px;color:var(--yellow)}
.partner-mark{left:368px;top:706px;width:82px;height:82px;border-radius:50%;background:#1f6d48}
.perk-text{left:177px;top:794px;width:840px;font-weight:300;font-size:18px;line-height:23px;color:var(--grey)}
.perk-text em{font-style:normal;color:var(--yellow)}
.readmore{left:174px;top:845px;font-weight:300;font-size:18px;color:var(--white);text-decoration:underline}

.footer-rule{left:172px;top:925px;width:856px;border-top:1px dotted #3d3e40}
.copyright{left:173px;top:944px;font-weight:300;font-size:13px;color:#4e4f51}
.footer-brand{left:854px;top:939px;width:172px;text-align:right;font-family:"Arvo",serif;font-size:26px;letter-spacing:-1px;color:var(--white)}
</style>
</head>
<body>
<div class="page">
  <div class="backdrop" role="img" aria-label="Dark photograph of an open office filing cabinet with hanging folders"></div>

  <div class="abs brand">VELMARIX</div>

  <div class="abs find">Find Profile:</div>
  <div class="abs find-field">
    <svg width="22" height="22" viewBox="0 0 22 22"><circle cx="8" cy="8" r="5.5" fill="none" stroke="#f6f23a" stroke-width="3"/><path d="M12 12l7 7" stroke="#f6f23a" stroke-width="4" stroke-linecap="round"/></svg>
    <span class="sep"></span>
  </div>

  <ul class="abs nav">
    <li><a href="#">HOME</a></li>
    <li><a href="#">ABOUT US</a></li>
    <li><a href="#">MY PROFILE</a></li>
    <li><a href="#">APP STORE</a></li>
    <li class="accent"><a href="#">CREAT AN ACCOUNT</a></li>
  </ul>

  <div class="abs login-band"></div>
  <svg class="abs numeral" style="left:508px;top:100px" width="135" height="150"><text x="0" y="143" font-size="172" textLength="132" lengthAdjust="spacingAndGlyphs">01</text></svg>
  <div class="abs num-dot" style="left:642px;top:231px"></div>
  <div class="abs login-title">LOGIN OR SIGN UP</div>
  <p class="abs login-intro">Use the form below if you already have an account. Both username and password are required to login</p>
  <div class="abs rule"></div>

  <div class="abs field" style="top:278px">
    <svg width="26" height="26" viewBox="0 0 26 26"><circle cx="13" cy="7" r="5.5" fill="#f6f23a"/><path d="M2 25c0-8 4-11 11-11s11 3 11 11z" fill="#f6f23a"/></svg>
    <span class="sep"></span><span>Enter Your User Name...</span>
  </div>
  <div class="abs field" style="top:326px">
    <svg width="26" height="26" viewBox="0 0 26 26"><circle cx="17" cy="8" r="6" fill="#f6f23a"/><circle cx="18" cy="7" r="2" fill="#1c1d20"/><path d="M13 12L4 21l2 3 2-2-1-2 2-1 1 1 6-6z" fill="#f6f23a"/></svg>
    <span class="sep"></span><span>Enter Your Password...</span>
  </div>
  <div class="abs options"><span class="checkbox"></span>Remember Me</div>
  <div class="abs forgot">Forgot Password? <a href="#">Click here</a></div>
  <div class="abs login-btn">LOGIN</div>

  <svg class="abs numeral" style="left:168px;top:406px" width="172" height="150"><text x="0" y="143" font-size="172" textLength="168" lengthAdjust="spacingAndGlyphs">02</text></svg>
  <div class="abs num-dot" style="left:340px;top:541px"></div>
  <div class="abs your">YOUR</div>
  <div class="abs job-tag">JOB SEARCH</div>
  <div class="abs starts">STARTS HERE...</div>
  <div class="abs cta">CREATE A PROFILE NOW</div>
  <svg class="abs cta-arrow" width="47" height="40" viewBox="0 0 47 40"><path d="M2 12h23V2l20 18-20 18V28H2z" fill="#fff"/></svg>

  <svg class="abs numeral" style="left:733px;top:634px" width="172" height="150"><text x="0" y="143" font-size="172" textLength="168" lengthAdjust="spacingAndGlyphs">03</text></svg>
  <div class="abs num-dot" style="left:901px;top:769px"></div>
  <div class="abs perk perk-lead">FEELING</div>
  <div class="abs partner-mark"></div>
  <div class="abs perk perk-partner">BREWMARK?</div>
  <p class="abs perk-text">For every 10 times your profile gets downloaded, you earn 1 brewmark coffee points. For every 10 brewmark coffee points, we ship a $10 brewmark card to your home. <em>ABSOLUTELY FREE!!!!</em></p>
  <a class="abs readmore" href="#">readmore...</a>

  <div class="abs footer-rule"></div>
  <div class="abs copyright">2013 @ Copyrights LARKFIELD. All rights reserved.</div>
  <div class="abs footer-brand">VELMARIX</div>
</div>
</body>
</html>
```